TOBREL Business Card Design

We need a business card design for a current Plastering company now moving to building and constructing new homes.
We have been in the Plastering(rendering) business for 15yrs and have made a good name with our customers for our Top Quality of work that we provide.
We would like TOBREL to be the main attraction with an image of architectural roof tops or house design within it. Blue Yellow and Black are colours we like but are willing to see other ideas.
We would like the design to be modern and communicate quality and experience.
Industry/Entity Type
Building
Contact Information for Business Card
TOBREL Building and Plastering
PO BOX 73519 Casuarina Darwin NT 0812
PH/Fax: 08 83170925 Email: tobrel@wavemail.example
Glen: 0419372654 Ruth:0408631597
ABN:57 208 931 446

```html
<!DOCTYPE html>
<html lang="en">
<head>
<meta charset="utf-8">
<title>TOBREL Building and Plastering – Business Card</title>
<link rel="stylesheet" href="https://fonts.googleapis.com/css2?family=Share+Tech+Mono&display=swap">
<style>
  :root {
    --page-bg: #ffffff;
    --card-dark: #0f0f0f;
    --card-mid: #2c2c2c;
    --card-glow: #4a4a4a;
    --artwork-tone: #a6b0ae;
    --artwork-light: #c4ccca;
    --brand-white: #ffffff;
  }
  html, body {
    margin: 0;
    padding: 0;
    width: 1200px;
    height: 741px;
    overflow: hidden;
    background: var(--page-bg);
  }
  .canvas {
    position: relative;
    width: 1200px;
    height: 741px;
  }
  .business-card {
    position: absolute;
    left: 44px;
    top: 43px;
    width: 1022px;
    height: 597px;
    overflow: hidden;
    background:
      radial-gradient(ellipse 520px 420px at 300px 230px, var(--card-glow) 0%, var(--card-mid) 35%, transparent 75%),
      linear-gradient(135deg, var(--card-mid) 0%, var(--card-dark) 55%, var(--card-dark) 100%);
  }
  .tower-artwork {
    position: absolute;
    left: 0;
    top: 0;
    width: 1022px;
    height: 597px;
  }
  .brand-block {
    position: absolute;
    left: 483px;
    top: 425px;
    width: 520px;
    font-family: "Share Tech Mono", monospace;
    color: var(--brand-white);
  }
  .brand-name {
    margin: 0;
    font-size: 120px;
    line-height: 100px;
    font-weight: 400;
    letter-spacing: 31px;
    white-space: nowrap;
  }
  .brand-tagline {
    margin: 6px 0 0;
    font-size: 27px;
    line-height: 32px;
    letter-spacing: 1.6px;
    white-space: nowrap;
  }
</style>
</head>
<body>
<div class="canvas">
  <section class="business-card">
    <svg class="tower-artwork" viewBox="0 0 1022 597" role="img"
         aria-label="Illustration of a high-rise tower under construction with a diagonal crane lattice across the top left corner">
      <defs>
        <linearGradient id="artworkTone" x1="0" y1="0" x2="1" y2="1">
          <stop offset="0" stop-color="var(--artwork-light)"/>
          <stop offset="1" stop-color="var(--artwork-tone)"/>
        </linearGradient>
      </defs>
      <path fill="url(#artworkTone)" opacity="0.85"
            d="M0 0 H520 L545 28 L250 247 V597 H52 V400 L0 420 Z"/>
    </svg>

    <div class="brand-block">
      <h1 class="brand-name">TOBREL</h1>
      <p class="brand-tagline">Building and Plastering</p>
    </div>
  </section>
</div>
</body>
</html>
```